3D Geology Modelling Web Design Project

I am a consultant who carries out 3D computer modelling for the mining and exploration industry. I am looking for a fully funcitonal corporate looking website for a small business and my logo is hosted at www.tarvolo.com.au. I will need around 7 pages or so (a description and sitemap are in a document called Tarvolo Website_brief.pdf , this document along with pictures and logo can be found at http://www.tarvolo.com.au/tarvolopics). The pages will be mostly static with some simple flash transitions and a simple enquiry form on a contact page. Otherwise just text and pics +/- flash. I will want to be able to update the pages myself, so what options are available for doing this (e.g. wordpress?). I also want it cross-browser and cross-platform friendly e.g. xhtml?

Similar style websites are:

http://www.pebblindrift.com.au/
http://www.ryvquarrying.com.au/
http://www.prismvale.com/Default.aspx
http://www.nolbeworld.com/
http://www.tuv.com/en
http://www.lodpfa.com/

Please have a look at the above samples to get a feel for what I am after. It’s a relatively simple standing site and I would want it done in a colour scheme that matches my logo which is blue and silver. I already have the domain name and hosting setup.

regards, Peter

Reason: Hi Everyone, I am extending the deadline for the final time just to give interested parties enough time to submit revisions. I will be choosing the final design on this deadline. Thanks, Peter

Target Market(s)

Geologists and Mining Companies varied ages male and female from 21-65 yo

Industry/Entity Type

Small Business

Requirements
Must have
• Cross platform and cross browser functionality e.g. can be seen in different browsers and on mobiles etc.. wirtten in xhtml?
Search Engine optimisation. LinkedIn connection?
Nice to have
• Some simple blending of header pictures with logo to give it a nice flow, rather than sharp discrete images. Some artistic licence is welcomed. Some flash style in banner? I have a lot of images and backgrounds to choose from now located on my website.

www.tarvolo.com/tarvolopics
Should not have
• No sounds

```html
<!DOCTYPE html>
<html lang="en">
<head>
<meta charset="utf-8">
<title>Tarvolo — Home</title>
<link rel="stylesheet" href="https://fonts.googleapis.com/css2?family=Cuprum:wght@400;700&display=swap">
<style>
  :root {
    --brand-blue: #0b6cb6;
    --heading-blue: #1c6fb4;
    --nav-grey: #9b9b9b;
    --nav-active: #4d4d4d;
    --body-grey: #8a8a8a;
    --tagline-grey: #a3a3a3;
    --rule: #c9c9c9;
    --icon-grey: #bdbdbd;
    --page: #ffffff;
    --paper: #efede6;
  }
  * { box-sizing: border-box; margin: 0; padding: 0; }
  html, body { width: 1200px; height: 1000px; overflow: hidden; }
  body {
    position: relative;
    background: linear-gradient(to bottom, var(--paper) 0, var(--page) 22px, var(--page) 100%);
    font-family: Arial, Helvetica, sans-serif;
  }
  .brand {
    position: absolute; left: 128px; top: 30px;
    display: flex; align-items: center; gap: 16px;
  }
  .brand-name {
    font-family: "Cuprum", sans-serif; font-weight: 700;
    font-size: 76px; line-height: 1; color: var(--brand-blue); letter-spacing: 1px;
  }
  .brand-mark { width: 58px; height: 58px; border-radius: 50%; border: 5px solid var(--brand-blue); }
  .social { position: absolute; right: 130px; top: 31px; display: flex; gap: 11px; }
  .social span { width: 17px; height: 17px; border-radius: 3px; background: var(--icon-grey); }
  .main-nav {
    position: absolute; left: 519px; top: 77px;
    display: flex; gap: 11px;
    font-family: "Cuprum", sans-serif; font-size: 20px; color: var(--nav-grey);
  }
  .main-nav a { color: inherit; text-decoration: none; padding: 0 0 10px; }
  .main-nav a.is-active {
    color: var(--nav-active); border-bottom: 1px solid var(--brand-blue);
    padding: 0 5px 10px; margin-right: 6px;
  }
  .hero {
    position: absolute; left: 120px; top: 144px; width: 960px; height: 447px;
    background: linear-gradient(to bottom, #1f2a1c 0%, #2c3529 18%, #6f737a 30%, #9a9ea5 55%, #7c8088 80%, #5d6068 100%);
    box-shadow: 0 12px 12px -8px rgba(0,0,0,.25);
  }
  .hero-badge {
    position: absolute; right: 4px; bottom: 4px; width: 150px; height: 58px;
    background: #fff; display: flex; align-items: center; justify-content: center;
    font-family: "Cuprum", sans-serif; font-weight: 700; font-size: 28px; color: var(--brand-blue);
  }
  .slider-dots { position: absolute; left: 586px; top: 616px; display: flex; gap: 5px; }
  .slider-dots span { width: 15px; height: 15px; border-radius: 50%; background: radial-gradient(circle at 40% 35%, #f2f2f2, #a8a8a8); border: 1px solid #9a9a9a; }
  .slider-dots span.is-current { background: radial-gradient(circle at 40% 35%, #d0d0d0, #7c7c7c); }
  .features { position: absolute; top: 656px; left: 130px; display: flex; }
  .feature { width: 320px; }
  .feature-head { display: flex; align-items: center; gap: 18px; height: 32px; }
  .feature-head h2 {
    font-family: "Cuprum", sans-serif; font-weight: 400; font-size: 24px;
    letter-spacing: 1.5px; color: var(--heading-blue);
  }
  .feature p { margin-top: 19px; width: 300px; font-size: 13px; line-height: 20px; color: var(--body-grey); }
  .rule { position: absolute; left: 127px; width: 941px; border-top: 1px solid var(--rule); }
  .callout {
    position: absolute; left: 129px; top: 844px;
    font-family: "Cuprum", sans-serif; font-size: 32px; color: var(--tagline-grey); letter-spacing: 0;
  }
  .button-explore {
    position: absolute; left: 921px; top: 844px; width: 149px; height: 39px;
    border: 1px solid #b8b8b8; background: linear-gradient(#f7f6f3, #e2e0db);
    font-family: "Cuprum", sans-serif; font-size: 24px; color: var(--heading-blue);
    display: flex; align-items: center; justify-content: center; letter-spacing: .5px;
  }
  .section-title {
    position: absolute; left: 131px; top: 967px;
    font-family: "Cuprum", sans-serif; font-weight: 400; font-size: 24px; color: var(--heading-blue);
  }
</style>
</head>
<body>
  <header>
    <div class="brand"><span class="brand-name">TARVOLO</span><span class="brand-mark"></span></div>
    <div class="social" aria-label="Social links"><span></span><span></span><span></span><span></span><span></span><span></span><span></span></div>
    <nav class="main-nav">
      <a class="is-active" href="#">HOME</a><a href="#">ABOUT</a><a href="#">SERVICES</a><a href="#">CLIENTS</a><a href="#">PUBLICATIONS</a><a href="#">TRAINING</a><a href="#">CONTACT</a>
    </nav>
  </header>

  <div class="hero" role="img" aria-label="Photograph of folded banded grey and white rock outcrop in front of a dark forest">
    <div class="hero-badge">TARVOLO</div>
  </div>
  <div class="slider-dots"><span></span><span class="is-current"></span></div>

  <section class="features">
    <article class="feature">
      <div class="feature-head">
        <svg width="32" height="32" viewBox="0 0 32 32"><circle cx="16" cy="16" r="14" fill="none" stroke="var(--icon-grey)" stroke-width="4"/><path d="M16 8v9h6" fill="none" stroke="var(--icon-grey)" stroke-width="3"/></svg>
        <h2>OUR MISSION</h2>
      </div>
      <p>Lorem ipsum dolor sit amet, consectetur adipiscing elit. Mauris varius pharetra esit commodo turstu adipiscing elit var pharetra ipsum dolor sit amet.</p>
    </article>
    <article class="feature">
      <div class="feature-head">
        <svg width="32" height="32" viewBox="0 0 32 32"><circle cx="16" cy="16" r="16" fill="var(--icon-grey)"/><path d="M8 16h16M11 12l-4 4 4 4M21 12l4 4-4 4" fill="none" stroke="#fff" stroke-width="2.5"/></svg>
        <h2>SERVICES</h2>
      </div>
      <p>Lorem ipsum dolor sit amet, consectetur adipiscing elit. Mauris varius pharetra esit commodo turstu adipiscing elit var pharetra ipsum dolor sit amet.</p>
    </article>
    <article class="feature">
      <div class="feature-head">
        <svg width="32" height="32" viewBox="0 0 32 32"><rect x="10" y="2" width="20" height="20" fill="none" stroke="var(--icon-grey)" stroke-width="4"/><rect x="2" y="10" width="20" height="20" fill="var(--icon-grey)"/><rect x="6" y="14" width="12" height="12" fill="#fff"/></svg>
        <h2>CLIENTS</h2>
      </div>
      <p>Lorem ipsum dolor sit amet, consectetur adipiscing elit. Mauris varius pharetra esit commodo turstu adipiscing elit var pharetra ipsum dolor sit amet.</p>
    </article>
  </section>

  <div class="rule" style="top:810px"></div>
  <p class="callout">TOP NOTCH SOLUTIONS FOR GEOLOGICAL MODELLING</p>
  <a class="button-explore">EXPLORE</a>
  <div class="rule" style="top:915px"></div>

  <h2 class="section-title">LATEST WORK</h2>
</body>
</html>
```